Flyer für Gästehaus am Bodensee
Zielgruppe
Es soll ein Hausprospekt in Form eines Wickelfalz Fylers (Standard Format, also 10x21 cm Endformat) für ein Gästehaus erstellt werden. Die Texte sollten von Ihnen erstellt werden. Dabei können Sie gerne die Texte der Internetseite (www.gaestehaus-wolkreiter.example) nutzen (entsprechend angepasst). Es werden auch zahlreiche Bilder vom Gästehaus und auch von Attraktionen in der Umgebung zur Verfügung gestellt (Wolkenfach Ablage: https://files.beispielablage.example/ordner?id=7KQ2ZtRmWpLx9NcVbDfGhJ). Diese dürfen aber nur für diese Ausschreibung verwendet werden!
Aufgabenstellung
- Der Flyer soll zeitlos sein (also auch in ein paar Jahren noch funktionieren)
- Der Flyer soll das Interesse am Haus und der Umgebung wecken (einige Ausflugsziele sollten erwähnt werden).
- Die Lage (Uhldingen-Mühlhofen bzw. Unteruhldingen) muss als Vorteil verkauft werden da von hier aus sehr viele Ausflugsziele gut erreicht werden können.
- Die Lage (quasi direkt am See) sollte erkenntlich sein.
- Die fertige Datei wird als PDF (für den Druck und für das Marketing) benötigt.
- Außerdem als Word Datei in der der Kunde selbst etwas ändern kann.
- Auch die Originaldatei von Ihrer Software möchten wir bei Abschluss erhalten.
- Alle Quelldateien (Bilder, Texte, Schriftarten usw.) gehen an uns über (inkl. aller Rechte und Lizenzen).
- Bitten nehmen Sie maximal ein Appartment als Beispiel im Flyer auf (es ist nicht zwangsläufig notwendig, es geht auch ganz ohne). In keinem Fall alle Appartments auflisten.

```html
<!DOCTYPE html>
<html lang="de">
<head>
<meta charset="utf-8">
<title>Gästehaus Wolkreiter – Wickelfalzflyer</title>
<link href="https://fonts.googleapis.com/css2?family=Josefin+Sans:ital,wght@1,300&family=Source+Sans+3:wght@400;600;700&display=swap" rel="stylesheet">
<style>
:root{
  --board:#58585a;
  --cream:#fdf4ea;
  --navy:#0b3f75;
  --blue:#0a72b5;
  --title:#1b7bbf;
  --label:#e6e6e6;
  --hint:#d0197b;
  --heading-font:"Josefin Sans", sans-serif;
  --body-font:"Source Sans 3", sans-serif;
}
*{margin:0;padding:0;box-sizing:border-box}
html,body{width:869px;height:1200px;overflow:hidden}
body{background:var(--board);position:relative;font-family:var(--body-font)}
.sheet{position:absolute;overflow:hidden;background:#fff;box-shadow:3px 3px 5px rgba(0,0,0,.45)}
.block{position:absolute}
.cream{background:var(--cream)}
.navy{background:var(--navy)}
.blue{background:var(--blue)}
.photo{position:absolute}
.caption{position:absolute;color:var(--label);font-size:12px;font-weight:400;letter-spacing:.2px;text-align:center}
.heading{position:absolute;font-family:var(--heading-font);font-weight:300;font-style:italic;font-size:9.2px;line-height:11.5px;color:var(--title);white-space:nowrap}
.on-dark .heading,.heading.light{color:#fff}
.subheading{position:absolute;font-size:5.8px;font-weight:400;color:var(--title);white-space:nowrap}
.copy{position:absolute;font-size:3.9px;line-height:6.5px;color:#3a3a3a}
.copy p{margin-bottom:6.5px}
.copy b{font-weight:700}
.on-dark .copy{color:#fff}
.copy .topic{display:block;font-weight:700;color:var(--title)}
.on-dark .copy .topic{color:#fff}
.logo{position:absolute;display:flex;align-items:center;gap:4px;font-size:9px;font-weight:400;color:#1f5d8f;white-space:nowrap}
.logo i{display:block;width:9px;height:9px;border-radius:50%;background:#1f5d8f}
.cover-title{position:absolute;left:0;width:145px;text-align:center;color:#fff}
.cover-title .heading{position:static;color:#fff;font-size:9px;line-height:12px;white-space:normal}
.cover-title .place{font-size:5.6px;margin-top:5px}
.contact-title{position:absolute;font-family:var(--heading-font);font-style:italic;font-weight:300;font-size:9px;color:#fff}
.map-hint{position:absolute;font-size:4.4px;line-height:6.5px;color:var(--hint)}
.map-sketch{position:absolute;border-radius:2px;background:linear-gradient(135deg,#1b5390,#2a6aa8)}
</style>
</head>
<body>

<!-- Titelseite -->
<div class="sheet" style="left:111px;top:37px;width:145px;height:305px">
  <div class="block cream" style="left:0;top:0;width:145px;height:48px">
    <div class="logo" style="left:27px;top:17px"><i></i>Gästehaus Wolkreiter</div>
  </div>
  <div class="photo" role="img" aria-label="Foto des Gästehauses mit Garten" style="left:0;top:50px;width:145px;height:147px;background:linear-gradient(180deg,#8fb8de 0%,#d8d3c8 30%,#b86a45 45%,#e6e2da 65%,#6e9a3e 85%,#5a8a2f 100%)"></div>
  <div class="block navy" style="left:0;top:200px;width:145px;height:52px">
    <div class="cover-title" style="top:7px">
      <div class="heading">Unser Haus –<br>Ihr Zuhause am Bodensee</div>
      <div class="place">In Uhldingen-Mühlhofen</div>
    </div>
  </div>
  <div class="photo" role="img" aria-label="Foto Segelboote im Hafen" style="left:0;top:254px;width:99px;height:51px;background:linear-gradient(180deg,#a9c6e4,#d6dde6 55%,#3d5f7e)"></div>
  <div class="photo" role="img" aria-label="Luftbild einer Insel im See" style="left:103px;top:254px;width:42px;height:51px;background:radial-gradient(circle at 45% 55%,#5f8d45 0 30%,#2b9fb2 50%,#1d6f9a)"></div>
</div>
<div class="caption" style="left:111px;top:357px;width:145px">Titelseite</div>

<!-- Flyer Innen aufgeklappt -->
<div class="sheet" style="left:329px;top:37px;width:435px;height:307px">
  <div class="photo" role="img" aria-label="Foto Segelregatta" style="left:0;top:0;width:71px;height:49px;background:linear-gradient(180deg,#b9cfe6,#e9eef2 60%,#6b8fb0)"></div>
  <div class="photo" role="img" aria-label="Foto Hausansicht mit Baum" style="left:75px;top:0;width:70px;height:49px;background:linear-gradient(180deg,#9fbfe0,#c98460 45%,#efece4 65%,#6d8f3d)"></div>
  <div class="photo" role="img" aria-label="Foto Frühstücksraum" style="left:146px;top:0;width:73px;height:49px;background:linear-gradient(180deg,#e9ddc8,#6b4330 70%,#3f2a20)"></div>
  <div class="photo" role="img" aria-label="Foto rote Blüten" style="left:221px;top:0;width:70px;height:49px;background:radial-gradient(circle at 50% 45%,#d92a3a 0 25%,#6fa43a 60%,#3f7a26)"></div>
  <div class="photo" role="img" aria-label="Foto Terrasse mit Sonnenschirm" style="left:293px;top:0;width:82px;height:49px;background:linear-gradient(180deg,#d8323a 0 25%,#86b84a 50%,#5e5a55)"></div>
  <div class="photo" role="img" aria-label="Foto Garten mit Pavillon" style="left:376px;top:0;width:59px;height:49px;background:linear-gradient(180deg,#a9cbe8,#7eb04a 55%,#4f8a2a)"></div>

  <div class="block cream" style="left:0;top:49px;width:435px;height:149px"></div>
  <div class="heading" style="left:18px;top:62px">Unser Haus - direkt am See</div>
  <div class="subheading" style="left:18px;top:80px">Ankommen und Wohlfühlen</div>
  <div class="copy" style="left:18px;top:91px;width:112px">
    <p>Das Gästehaus Wolkreiter liegt in einer der schönsten Urlaubsgegenden der Bodensee-Region, in Unteruhldingen, zwischen Meersburg und Überlingen, nur 50 Meter vom See entfernt, gegenüber der Blüteninsel Seewerth. Die schönsten Ausflugsziele am See erreichen Sie innerhalb kurzer Zeit.</p>
    <p>Für Gäste, die mit dem Auto anreisen, stehen Parkplätze direkt vor dem Haus zur Verfügung. Wer mit der Bahn zu uns kommt, wird auf Wunsch vom Bahnhof in Oberuhldingen abgeholt. Er weiß es bestimmt zu schätzen, dass die Bushaltestelle nur ein paar Schritte vom Haus entfernt ist.</p>
  </div>
  <div class="copy" style="left:164px;top:72px;width:112px">
    <p>Zur Schiffsanlegestelle in der Ortsmitte sind es zu Fuß auch nur 10 Minuten – ein wunderschöner Spaziergang, teilweise am See entlang. Sie können bei uns im Haus auch Fahrräder für Kurzausflüge mieten. Fahrradfahrer finden bei uns Unterstellmöglichkeiten für ihre Räder.</p>
  </div>
  <div class="copy" style="left:311px;top:72px;width:112px">
    <p>Unsere schöne Liegewiese und der gepflegte Garten sind das richtige Ambiente, wenn Sie sich erholen und ein wenig die Seele baumeln lassen wollen oder nach einem ereignisreichen Urlaubstag sich noch mit anderen Gästen zu einem kleinen Plausch treffen möchten.</p>
  </div>

  <div class="block blue" style="left:146px;top:126px;width:289px;height:3px"></div>
  <div class="block navy on-dark" style="left:146px;top:129px;width:289px;height:69px">
    <div class="heading" style="left:18px;top:13px;font-size:9.4px;line-height:12.2px">Appartements –<br>komfortables<br>Wohnen</div>
  </div>
  <div class="photo" role="img" aria-label="Foto Schlafzimmer" style="left:236px;top:143px;width:51px;height:55px;background:linear-gradient(180deg,#e9dcc2,#c7914f 55%,#b9462f)"></div>
  <div class="photo" role="img" aria-label="Foto Wohnzimmer mit Balkontür" style="left:293px;top:143px;width:69px;height:55px;background:linear-gradient(180deg,#dfe0d6,#8fae6a 40%,#6b4a3a 75%,#4f5f86)"></div>
  <div class="photo" role="img" aria-label="Foto Essecke mit Küche" style="left:369px;top:143px;width:60px;height:55px;background:linear-gradient(180deg,#f0e6d4,#c86a38 60%,#4b5d8c)"></div>

  <div class="photo" role="img" aria-label="Foto Appartement mit Sofa und Essecke" style="left:0;top:198px;width:146px;height:109px;background:linear-gradient(180deg,#e8e2d6 0%,#b89a74 45%,#7a5640 70%,#d9cdbb 100%)"></div>
  <div class="block blue on-dark" style="left:146px;top:198px;width:289px;height:109px">
    <div class="copy" style="left:18px;top:14px;width:114px">
      <p>Unsere Zimmer und Appartements sind komfortabel ausgestattet, damit Sie einen angenehmen und entspannten Urlaub verbringen. Alle Appartements verfügen über eine Dusche / WC, Küche, Balkon (teilweise mit Seesicht) oder Terrasse. TV, Telefon, W-LAN, Safe, Bettwäsche und Handtücher gehören ebenso zur Ausstattung und sind inklusiv.</p>
      <p>Wir haben ausschließlich Nichtraucherzimmer. Gerne können Sie auf dem Balkon oder der Terrasse rauchen. Bitte beachten Sie außerdem, dass in unserem Haus keine Tiere gestattet sind.</p>
    </div>
    <div class="copy" style="left:165px;top:14px;width:114px">
      <p>Ob Sie geschäftlich unterwegs sind oder Ihren Urlaub bei uns verbringen, wir sind stets bemüht, dass Sie sich bei uns wohl fühlen. Bei uns erwartet Sie eine herzliche und familiäre Atmosphäre. Die herrliche Umgebung und die optimale Lage unseres Hauses öffnen unzählige Ausflugsmöglichkeiten für Groß und Klein.</p>
      <p>Auf Wunsch verwöhnen wir Sie auch mit einem reichhaltigen Frühstück.</p>
      <p>Genauere Zimmerbeschreibungen und Preise finden Sie unter <b>www.gaestehaus-wolkreiter.example</b></p>
    </div>
  </div>
</div>
<div class="caption" style="left:329px;top:357px;width:435px">Flyer Innen aufgeklappt</div>

<!-- Flyer Innen erste Seite und Einklapper -->
<div class="sheet" style="left:111px;top:413px;width:286px;height:305px">
  <div class="photo" role="img" aria-label="Foto Segelregatta" style="left:0;top:0;width:70px;height:49px;background:linear-gradient(180deg,#b9cfe6,#e9eef2 60%,#6b8fb0)"></div>
  <div class="photo" role="img" aria-label="Foto Hausansicht mit Baum" style="left:75px;top:0;width:70px;height:49px;background:linear-gradient(180deg,#9fbfe0,#c98460 45%,#efece4 65%,#6d8f3d)"></div>
  <div class="photo" role="img" aria-label="Foto Thermalbad mit Außenbecken" style="left:146px;top:0;width:66px;height:49px;background:linear-gradient(180deg,#2a6fb0,#1c2c3c 45%,#38b4d8 75%,#9fe0ee)"></div>
  <div class="photo" role="img" aria-label="Foto Kinder im Affenpark" style="left:217px;top:0;width:69px;height:49px;background:linear-gradient(180deg,#8bb65a,#c9a27a 50%,#6d8a3a)"></div>

  <div class="block cream" style="left:0;top:49px;width:145px;height:150px">
    <div class="heading" style="left:18px;top:13px">Unser Haus - direkt am See</div>
    <div class="subheading" style="left:18px;top:31px">Ankommen und Wohlfühlen</div>
    <div class="copy" style="left:18px;top:42px;width:112px">
      <p>Das Gästehaus Wolkreiter liegt in einer der schönsten Urlaubsgegenden der Bodensee-Region, in Unteruhldingen, zwischen Meersburg und Überlingen, nur 50 Meter vom See entfernt, gegenüber der Blüteninsel Seewerth. Die schönsten Ausflugsziele am See erreichen Sie innerhalb kurzer Zeit.</p>
      <p>Für Gäste, die mit dem Auto anreisen, stehen Parkplätze direkt vor dem Haus zur Verfügung. Wer mit der Bahn zu uns kommt, wird auf Wunsch vom Bahnhof in Oberuhldingen abgeholt. Er weiß es bestimmt zu schätzen, dass die Bushaltestelle nur ein paar Schritte vom Haus entfernt ist.</p>
    </div>
  </div>
  <div class="photo" role="img" aria-label="Foto Appartement mit Sofa und Essecke" style="left:0;top:199px;width:145px;height:106px;background:linear-gradient(180deg,#e8e2d6 0%,#b89a74 45%,#7a5640 70%,#d9cdbb 100%)"></div>

  <div class="block navy on-dark" style="left:145px;top:49px;width:141px;height:147px">
    <div class="heading" style="left:18px;top:13px">Ausflugsziele und Aktivitäten</div>
    <div class="copy" style="left:18px;top:31px;width:112px">
      <p><span class="topic">Thermalbäder</span>Für Ihr Verwöhnprogramm stehen die Thermen der Nachbarorte mit ihren Wellness-Bereichen (z. B. Kaskadenbecken mit Unterwassermusik, Ruhebereiche mit Blick über den See) zur Verfügung.</p>
      <p><span class="topic">Affenpark im Hinterland</span>Kinder haben besonders viel Spaß, wenn sie im Affenpark die Berberaffen beobachten und füttern können.</p>
      <p><span class="topic">Blüteninsel Seewerth</span>Weltbekannt ist die Blüteninsel Seewerth, die Sie im Frühling und im Herbst vom Gästehaus Wolkreiter aus sehen können. Von der Schiffsanlegestelle in Unteruhldingen können Sie mit dem Schiff hinüber fahren und Rosen und Orchideen genießen.</p>
    </div>
  </div>
  <div class="photo" role="img" aria-label="Foto Schloss mit Kirche und Blumengarten" style="left:146px;top:199px;width:140px;height:106px;background:linear-gradient(180deg,#4f8fd0 0%,#b8d4ee 30%,#e7b9a2 50%,#5f9b3a 75%,#4e8f2b 100%)"></div>
</div>
<div class="caption" style="left:111px;top:735px;width:286px">Flyer Innen erste Seite und Einklapper</div>

<!-- Rückseite -->
<div class="sheet" style="left:470px;top:413px;width:145px;height:305px">
  <div class="photo" role="img" aria-label="Foto Pfahlbauten am Steg" style="left:0;top:0;width:92px;height:49px;background:linear-gradient(180deg,#a9c6e8,#e5ecf2 40%,#8a6a48 60%,#4f7a64)"></div>
  <div class="photo" role="img" aria-label="Foto Wallfahrtskirche über dem See" style="left:96px;top:0;width:49px;height:49px;background:linear-gradient(180deg,#a9c6e8,#e9d7c0 40%,#5f8f3a 70%,#4b7a5c)"></div>
  <div class="block cream" style="left:0;top:49px;width:145px;height:111px">
    <div class="heading" style="left:18px;top:10px">Perfekte Lage</div>
    <div class="copy" style="left:18px;top:27px;width:115px">
      <p><span class="topic">Pfahlbauten und Wallfahrtskirche am Hang</span>Uhldingen-Mühlhofen selbst beherbergt zwei der schönsten Ausflugsziele am See: die Pfahlbauten und die Wallfahrtskirche mit ihrem traumhaften Blick über den Bodensee.</p>
      <p><span class="topic">Alte Schlösser und Burgen</span>Wenn Sie Geschichte und die Romantik alter Schlösser und Burgen lieben, dann gefällt Ihnen sicher Überlingen, die alte Reichsstadt oder Meersburg mit der Alten Burg und dem Neuen Schloss. Sie alle sind mit dem Auto von unserem Haus aus in circa einer Viertelstunde zu erreichen.</p>
    </div>
  </div>
  <div class="block blue on-dark" style="left:0;top:160px;width:145px;height:36px">
    <div class="copy" style="left:18px;top:4px;width:117px">Übrigens: Mit dem <b>Seeland-Erlebnispass</b> haben Sie freien Eintritt und freie Fahrt bei rund 180 Erlebniszielen rund um den See, in Deutschland, Österreich, der Schweiz und dem Fürstentum Liechtenstein.</div>
  </div>
  <div class="block navy on-dark" style="left:0;top:199px;width:145px;height:106px">
    <div class="contact-title" style="left:18px;top:21px">Kontakt</div>
    <div class="map-hint" style="left:80px;top:20px">Hier könnte ein<br>Lageplan stehen</div>
    <div class="map-sketch" role="img" aria-label="Platz für Lageplan-Skizze" style="left:82px;top:37px;width:50px;height:30px"></div>
    <div class="copy" style="left:18px;top:40px;width:70px">
      <p>Familie Wolkreiter<br>Oberer Wiesenweg 4<br>12345 Uhldingen-Mühlhofen</p>
      <p>Tel. 0 12 34 / 90 12<br>Fax 0 12 34 / 90 13<br>info@gaestehaus-wolkreiter.example</p>
    </div>
  </div>
</div>
<div class="caption" style="left:470px;top:735px;width:145px">Rückseite</div>

<!-- Flyer Aussen aufgeklappt -->
<div class="sheet" style="left:329px;top:788px;width:435px;height:307px">
  <div class="photo" role="img" aria-label="Foto Thermalbad mit Außenbecken" style="left:0;top:0;width:68px;height:49px;background:linear-gradient(180deg,#2a6fb0,#1c2c3c 45%,#38b4d8 75%,#9fe0ee)"></div>
  <div class="photo" role="img" aria-label="Foto Kinder im Affenpark" style="left:72px;top:0;width:71px;height:49px;background:linear-gradient(180deg,#8bb65a,#c9a27a 50%,#6d8a3a)"></div>
  <div class="photo" role="img" aria-label="Foto Pfahlbauten am Steg" style="left:143px;top:0;width:93px;height:49px;background:linear-gradient(180deg,#a9c6e8,#e5ecf2 40%,#8a6a48 60%,#4f7a64)"></div>
  <div class="photo" role="img" aria-label="Foto Wallfahrtskirche über dem See" style="left:240px;top:0;width:49px;height:49px;background:linear-gradient(180deg,#a9c6e8,#e9d7c0 40%,#5f8f3a 70%,#4b7a5c)"></div>
  <div class="block cream" style="left:289px;top:0;width:146px;height:48px">
    <div class="logo" style="left:28px;top:17px"><i></i>Gästehaus Wolkreiter</div>
  </div>

  <div class="block navy on-dark" style="left:0;top:49px;width:141px;height:149px">
    <div class="heading" style="left:18px;top:13px">Ausflugsziele und Aktivitäten</div>
    <div class="copy" style="left:18px;top:31px;width:112px">
      <p><span class="topic">Thermalbäder</span>Für Ihr Verwöhnprogramm stehen die Thermen der Nachbarorte mit ihren Wellness-Bereichen (z. B. Kaskadenbecken mit Unterwassermusik, Ruhebereiche mit Blick über den See) zur Verfügung.</p>
      <p><span class="topic">Affenpark im Hinterland</span>Kinder haben besonders viel Spaß, wenn sie im Affenpark die Berberaffen beobachten und füttern können.</p>
      <p><span class="topic">Blüteninsel Seewerth</span>Weltbekannt ist die Blüteninsel Seewerth, die Sie im Frühling und im Herbst vom Gästehaus Wolkreiter aus sehen können. Von der Schiffsanlegestelle in Unteruhldingen können Sie mit dem Schiff hinüber fahren und Rosen und Orchideen genießen.</p>
    </div>
  </div>
  <div class="photo" role="img" aria-label="Foto Schloss mit Kirche und Blumengarten" style="left:0;top:201px;width:141px;height:106px;background:linear-gradient(180deg,#4f8fd0 0%,#b8d4ee 30%,#e7b9a2 50%,#5f9b3a 75%,#4e8f2b 100%)"></div>

  <div class="block cream" style="left:141px;top:49px;width:148px;height:113px">
    <div class="heading" style="left:18px;top:10px">Perfekte Lage</div>
    <div class="copy" style="left:18px;top:27px;width:118px">
      <p><span class="topic">Pfahlbauten und Wallfahrtskirche am Hang</span>Uhldingen-Mühlhofen selbst beherbergt zwei der schönsten Ausflugsziele am See: die Pfahlbauten und die Wallfahrtskirche mit ihrem traumhaften Blick über den Bodensee.</p>
      <p><span class="topic">Alte Schlösser und Burgen</span>Wenn Sie Geschichte und die Romantik alter Schlösser und Burgen lieben, dann gefällt Ihnen sicher Überlingen, die alte Reichsstadt oder Meersburg mit der Alten Burg und dem Neuen Schloss. Sie alle sind mit dem Auto von unserem Haus aus in circa einer Viertelstunde zu erreichen.</p>
    </div>
  </div>
  <div class="block blue on-dark" style="left:141px;top:162px;width:148px;height:36px">
    <div class="copy" style="left:18px;top:4px;width:120px">Übrigens: Mit dem <b>Seeland-Erlebnispass</b> haben Sie freien Eintritt und freie Fahrt bei rund 180 Erlebniszielen rund um den See, in Deutschland, Österreich, der Schweiz und dem Fürstentum Liechtenstein.</div>
  </div>
  <div class="block navy on-dark" style="left:141px;top:201px;width:148px;height:106px">
    <div class="contact-title" style="left:18px;top:21px">Kontakt</div>
    <div class="map-hint" style="left:81px;top:20px">Hier könnte ein<br>Lageplan stehen</div>
    <div class="map-sketch" role="img" aria-label="Platz für Lageplan-Skizze" style="left:84px;top:37px;width:50px;height:30px"></div>
    <div class="copy" style="left:18px;top:40px;width:70px">
      <p>Familie Wolkreiter<br>Oberer Wiesenweg 4<br>12345 Uhldingen-Mühlhofen</p>
      <p>Tel. 0 12 34 / 90 12<br>Fax 0 12 34 / 90 13<br>info@gaestehaus-wolkreiter.example</p>
    </div>
  </div>

  <div class="photo" role="img" aria-label="Foto des Gästehauses mit Garten" style="left:289px;top:49px;width:146px;height:150px;background:linear-gradient(180deg,#8fb8de 0%,#d8d3c8 30%,#b86a45 45%,#e6e2da 65%,#6e9a3e 85%,#5a8a2f 100%)"></div>
  <div class="block navy" style="left:289px;top:201px;width:146px;height:106px">
    <div class="cover-title" style="top:6px;width:146px">
      <div class="heading">Unser Haus –<br>Ihr Zuhause am Bodensee</div>
      <div class="place">In Uhldingen-Mühlhofen</div>
    </div>
  </div>
  <div class="photo" role="img" aria-label="Foto Segelboote im Hafen" style="left:289px;top:255px;width:100px;height:52px;background:linear-gradient(180deg,#a9c6e4,#d6dde6 55%,#3d5f7e)"></div>
  <div class="photo" role="img" aria-label="Luftbild einer Insel im See" style="left:393px;top:255px;width:42px;height:52px;background:radial-gradient(circle at 45% 55%,#5f8f45 0 30%,#2b9fb2 50%,#1d6f9a)"></div>
</div>
<div class="caption" style="left:329px;top:1112px;width:435px">Flyer Aussen aufgeklappt</div>

</body>
</html>
```